Emergency Management Consulting Flyer

Company name: Stone Harbor Emergency Management

I am looking for a postcard design for my emergency management consulting business. I'm looking for something that has some colors and is double sided, on side with the information on services provided and the other side with the contact information. For the main side I'm looking for the following:

How prepared are you?

Services Provided:
Healthcare Preparedness
EOC Support
Emergency Planning
Mitigation Planning
Business Continuity
Disaster Response
Training and Exercises
Project Management
And more

Affordable for small and large organizations
Stand-by contracts available

On the back side, I'm looking for Contact Us section.

Overall I'm looking for something a bit more modern and need to have at least one disaster photo. If you have questions please message me.

Target Market(s)

Government, Healthcare Facilities, Businesses

Industry/Entity Type

Consulting

Requirements
Must have
• Disaster Picture, modern looking
• For the main side I'm looking for the following:
• How prepared are you?
• Services Provided:
• Healthcare Preparedness
• EOC Support
• Emergency Planning
• Mitigation Planning
• Business Continuity
• Disaster Response
• Training and Exercises
• Project Management
• And more
• Affordable for small and large organizations
• Stand-by contracts available

```html
<!DOCTYPE html>
<html lang="en">
<head>
<meta charset="utf-8">
<title>Stone Harbor Emergency Management – Postcard</title>
<link rel="stylesheet" href="https://fonts.googleapis.com/css2?family=Bebas+Neue&family=Lato:wght@400;700&family=Roboto+Condensed:wght@300;700&display=swap">
<style>
  :root{
    --orange:#e8622a;
    --navy:#1f3f8f;
    --charcoal:#555555;
    --ink:#333333;
    --band-grey:#e2e2e2;
    --stamp:#ebebeb;
    --paper:#ffffff;
  }
  *{margin:0;padding:0;box-sizing:border-box;}
  html,body{width:1200px;height:1200px;overflow:hidden;background:var(--paper);}
  .canvas{position:relative;width:1200px;height:1200px;background:var(--paper);}
  .postcard{position:absolute;width:698px;height:540px;background:var(--paper);box-shadow:0 2px 14px rgba(0,0,0,.18);overflow:hidden;}
  .postcard--front{left:253px;top:40px;}
  .postcard--back{left:255px;top:612px;}
  .postcard svg{display:block;width:698px;height:540px;}
  .brand-name{font-family:'Lato',sans-serif;font-weight:700;fill:var(--ink);}
  .headline{font-family:'Bebas Neue',sans-serif;}
  .headline--orange{fill:var(--orange);}
  .headline--navy{fill:var(--navy);}
  .service{font-family:'Lato',sans-serif;font-size:20px;fill:var(--ink);}
  .contact-phone,.contact-web{font-family:'Lato',sans-serif;}
  .on-dark{fill:#ffffff;}
  .on-light{fill:var(--ink);}
  .offer-strong{font-family:'Roboto Condensed',sans-serif;font-weight:700;fill:var(--orange);}
  .offer-light{font-family:'Roboto Condensed',sans-serif;font-weight:300;fill:var(--navy);}
  .offer-note{font-family:'Lato',sans-serif;fill:var(--orange);}
</style>
</head>
<body>
<main class="canvas">

  <!-- Front side: services -->
  <section class="postcard postcard--front">
    <svg viewBox="0 0 873 675" xmlns="http://www.w3.org/2000/svg">
      <defs>
        <linearGradient id="meetingTones" x1="0" y1="0" x2="1" y2="1">
          <stop offset="0" stop-color="#d9dde2"/>
          <stop offset=".45" stop-color="#9aa3b3"/>
          <stop offset="1" stop-color="#c7ccd2"/>
        </linearGradient>
        <linearGradient id="portraitTones" x1="0" y1="0" x2="1" y2="1">
          <stop offset="0" stop-color="#dbe8f2"/>
          <stop offset="1" stop-color="#9fbad0"/>
        </linearGradient>
      </defs>

      <!-- brand -->
      <circle cx="56" cy="62" r="26" fill="var(--navy)"/>
      <text class="brand-name" x="104" y="75" font-size="32" textLength="265" lengthAdjust="spacingAndGlyphs">STONE HARBOR</text>
      <text class="brand-name" x="104" y="91" font-size="13" textLength="265" lengthAdjust="spacingAndGlyphs">EMERGENCY MANAGEMENT</text>

      <!-- headline -->
      <text class="headline headline--orange" x="38" y="175" font-size="66" textLength="320" lengthAdjust="spacingAndGlyphs">HOW PREPARED</text>
      <text class="headline headline--navy" x="36" y="275" font-size="118" textLength="318" lengthAdjust="spacingAndGlyphs">ARE YOU?</text>

      <!-- services -->
      <g class="service-list">
        <g><circle cx="45" cy="310" r="10" fill="var(--orange)"/><circle cx="45" cy="310" r="5" fill="none" stroke="#fff" stroke-width="2"/><text class="service" x="65" y="317">Healthcare Preparedness</text></g>
        <g><circle cx="45" cy="343" r="10" fill="var(--orange)"/><circle cx="45" cy="343" r="5" fill="none" stroke="#fff" stroke-width="2"/><text class="service" x="65" y="350">EOC Support</text></g>
        <g><circle cx="45" cy="375" r="10" fill="var(--orange)"/><circle cx="45" cy="375" r="5" fill="none" stroke="#fff" stroke-width="2"/><text class="service" x="65" y="382">Emergency Planning</text></g>
        <g><circle cx="45" cy="408" r="10" fill="var(--orange)"/><circle cx="45" cy="408" r="5" fill="none" stroke="#fff" stroke-width="2"/><text class="service" x="65" y="415">Mitigation Planning</text></g>
        <g><circle cx="45" cy="440" r="10" fill="var(--orange)"/><circle cx="45" cy="440" r="5" fill="none" stroke="#fff" stroke-width="2"/><text class="service" x="65" y="447">Business Continuity</text></g>
        <g><circle cx="45" cy="473" r="10" fill="var(--orange)"/><circle cx="45" cy="473" r="5" fill="none" stroke="#fff" stroke-width="2"/><text class="service" x="65" y="480">Disaster Response</text></g>
        <g><circle cx="45" cy="505" r="10" fill="var(--orange)"/><circle cx="45" cy="505" r="5" fill="none" stroke="#fff" stroke-width="2"/><text class="service" x="65" y="512">Training and Exercises</text></g>
        <g><circle cx="45" cy="536" r="10" fill="var(--orange)"/><circle cx="45" cy="536" r="5" fill="none" stroke="#fff" stroke-width="2"/><text class="service" x="65" y="544">Project Management</text></g>
        <text class="service" x="65" y="567">And more</text>
      </g>

      <!-- hero arcs and photo area -->
      <ellipse cx="950" cy="300" rx="580" ry="400" fill="var(--orange)"/>
      <ellipse cx="950" cy="300" rx="562" ry="382" fill="#ffffff"/>
      <ellipse cx="950" cy="300" rx="558" ry="378" fill="var(--navy)"/>
      <ellipse cx="950" cy="300" rx="536" ry="356" fill="#ffffff"/>
      <ellipse cx="950" cy="300" rx="532" ry="352" fill="url(#meetingTones)" role="img" aria-label="Photo of a consulting team planning around a table with site maps"/>

      <!-- portrait inset -->
      <circle cx="411" cy="475" r="118" fill="var(--orange)"/>
      <circle cx="411" cy="475" r="111" fill="#ffffff"/>
      <circle cx="411" cy="475" r="107" fill="url(#portraitTones)" role="img" aria-label="Photo of a smiling consultant in an office"/>

      <!-- contact band -->
      <path d="M0 593 H300 C350 593 380 605 429 675 H0 Z" fill="var(--charcoal)"/>
      <path d="M38 610 c-3 4 -1 12 6 17 c3 2 5 2 7 0 l-3 -4 l-3 2 c-3 -2 -5 -6 -4 -9 l3 -1 l-2 -5 Z" fill="var(--orange)"/>
      <text class="contact-phone on-dark" x="60" y="628" font-size="30">0123456789</text>
      <circle cx="45" cy="645" r="8" fill="var(--orange)"/>
      <text class="contact-web on-dark" x="60" y="652" font-size="20">www.companywebsite.com</text>
    </svg>
  </section>

  <!-- Back side: contact -->
  <section class="postcard postcard--back">
    <svg viewBox="0 0 873 675" xmlns="http://www.w3.org/2000/svg">
      <defs>
        <clipPath id="backPanel"><ellipse cx="40" cy="150" rx="395" ry="385"/></clipPath>
        <linearGradient id="coastTones" x1="0" y1="0" x2="0" y2="1">
          <stop offset="0" stop-color="#7b8593"/>
          <stop offset=".45" stop-color="#b7c0c8"/>
          <stop offset=".65" stop-color="#3d4750"/>
          <stop offset="1" stop-color="#6f8797"/>
        </linearGradient>
      </defs>

      <ellipse cx="40" cy="150" rx="436" ry="420" fill="var(--orange)"/>
      <ellipse cx="40" cy="150" rx="420" ry="404" fill="#ffffff"/>
      <ellipse cx="40" cy="150" rx="417" ry="401" fill="var(--navy)"/>
      <ellipse cx="40" cy="150" rx="395" ry="385" fill="#ffffff"/>

      <g clip-path="url(#backPanel)">
        <rect x="0" y="282" width="873" height="88" fill="var(--band-grey)"/>
        <rect x="0" y="370" width="873" height="200" fill="url(#coastTones)" role="img" aria-label="Photo of storm waves breaking over a rocky shoreline"/>
      </g>

      <!-- brand -->
      <circle cx="58" cy="84" r="24" fill="var(--navy)"/>
      <text class="brand-name" x="97" y="92" font-size="30" textLength="234" lengthAdjust="spacingAndGlyphs">STONE HARBOR</text>
      <text class="brand-name" x="97" y="106" font-size="12" textLength="234" lengthAdjust="spacingAndGlyphs">EMERGENCY MANAGEMENT</text>

      <!-- offer -->
      <text class="offer-strong" x="35" y="176" font-size="31" textLength="301" lengthAdjust="spacingAndGlyphs">Affordable for small and</text>
      <text class="offer-light" x="35" y="216" font-size="44" textLength="306" lengthAdjust="spacingAndGlyphs">large organizations</text>
      <text class="offer-note" x="35" y="245" font-size="24" textLength="307" lengthAdjust="spacingAndGlyphs">Stand-by contracts available</text>

      <!-- contact -->
      <path d="M38 300 c-3 4 -1 12 6 17 c3 2 5 2 7 0 l-3 -4 l-3 2 c-3 -2 -5 -6 -4 -9 l3 -1 l-2 -5 Z" fill="var(--orange)"/>
      <text class="contact-phone on-light" x="60" y="325" font-size="33">0123456789</text>
      <circle cx="44" cy="345" r="9" fill="var(--orange)"/>
      <text class="contact-web on-light" x="60" y="352" font-size="22">www.companywebsite.com</text>

      <!-- stamp area -->
      <rect x="721" y="20" width="125" height="145" fill="var(--stamp)"/>
    </svg>
  </section>

</main>
</body>
</html>
```